Golden Coat All-Purpose Breading Bag Design

Our client, Halvern Food Products, is looking to re-design the packaging for their product, Pellow's Golden Coat. Goldn Coat is an all-purpose food breading mix.

Halvern Foods has a registered trademark for this product, but they have not been using it for this particular 10 pound bag. They want to get the trademark onto the bag and also give the bag an updated look. They would like to continue to use the same red and blue colors. This 10 pound bag is not available on store shelves; it is sold to food service distributors who sell to restaurants.

All of the copy on the existing bag is still relevant, so we will want to incoprporate it into the bag design. Once these bags are filled with product, the tops get folded over about 1 inch and then sewn shut with thread.

Eventually, we will need the design applied to the Bag Template file attached, but that isn't important until a design is selected.

Target Market(s)

Restaurants

Industry/Entity Type

Food Manufacturing

Colors
0054AA
0677BA
7BADD7
CADEEF
E8F1F8
EB3D1F
EC4F4E
F09395
F8D3D4
FCEDEE

Requirements
Must have
• Trademark introduced to the design

```html
<!DOCTYPE html>
<html lang="en">
<head>
<meta charset="utf-8">
<title>Pellow's Golden Coat – 10 lb Breading Bag</title>
<link rel="stylesheet" href="https://fonts.googleapis.com/css2?family=Arimo:wght@400;700&display=swap">
<style>
  :root {
    --blue: #1f5fae;
    --blue-deep: #0054aa;
    --red: #eb3d1f;
    --white: #ffffff;
    --backdrop: #e4e4e6;
    --ink: #111111;
  }
  * { box-sizing: border-box; margin: 0; padding: 0; }
  html, body { width: 1200px; height: 1200px; overflow: hidden; }
  body {
    background: var(--backdrop);
    font-family: "Arimo", Arial, sans-serif;
    position: relative;
  }

  /* ---------- front panel ---------- */
  .bag-front {
    position: absolute;
    left: 280px; top: 30px;
    width: 470px; height: 1140px;
    background: var(--white);
    overflow: hidden;
  }
  .edge-strip {
    position: absolute; left: 0; width: 18px;
    top: 203px; height: 837px;
    background: var(--blue);
  }
  .edge-accent {
    position: absolute; left: 0; width: 18px; height: 22px;
    background: var(--red);
  }
  .edge-accent--top { top: 212px; }
  .edge-accent--bottom { top: 960px; }
  .main-panel {
    position: absolute; left: 0; right: 0;
    top: 236px; height: 804px;
    background: var(--blue);
  }
  .brand-box {
    position: absolute; left: 18px; right: 8px;
    top: 0; height: 375px;
    background: var(--white);
    display: flex; flex-direction: column;
    align-items: center; justify-content: center;
  }
  .brand-name {
    color: var(--red);
    font-weight: 700;
    text-align: center;
    line-height: 1.02;
    text-transform: uppercase;
  }
  .brand-name__owner { font-size: 54px; }
  .brand-name__product { font-size: 82px; }
  .trademark { font-size: 0.45em; vertical-align: super; }
  .maker {
    position: absolute; left: 34px; right: 8px; top: 640px;
    color: var(--white);
  }
  .maker__name { font-size: 26px; font-weight: 700; white-space: nowrap; }
  .maker__address {
    margin-left: 56px; margin-top: 6px;
    font-size: 19px; font-weight: 700; line-height: 1.3;
  }
  .selling-copy {
    position: absolute; left: 18px; right: 8px; top: 806px;
    color: var(--white); text-align: center;
  }
  .selling-copy__title { font-size: 28px; font-weight: 700; line-height: 1.2; }
  .selling-copy__tag { font-size: 13px; line-height: 1.3; }
  .selling-copy__detail { font-size: 13px; line-height: 1.3; }
  .selling-copy__slogan { font-size: 21px; line-height: 1.3; margin-top: 4px; }
  .ingredients {
    position: absolute; left: 18px; width: 430px; top: 944px; height: 92px;
    background: var(--white);
    padding: 10px 12px 0;
    font-size: 16px; font-weight: 700; line-height: 1.25;
    color: var(--ink); text-align: center;
    text-transform: uppercase;
  }
  .right-accent {
    position: absolute; right: 0; width: 22px; top: 1000px; height: 22px;
    background: var(--red);
  }
  .net-weight-bar {
    position: absolute; left: 0; right: 0; top: 1052px; height: 8px;
    background: var(--blue);
  }
  .net-weight {
    position: absolute; left: 130px; width: 200px; top: 1038px; height: 34px;
    background: var(--blue);
    color: var(--white);
    font-size: 20px; font-weight: 700;
    display: flex; align-items: center; justify-content: center;
  }

  /* ---------- side gusset ---------- */
  .bag-side {
    position: absolute;
    left: 750px; top: 30px;
    width: 180px; height: 1140px;
    background: var(--white);
    overflow: hidden;
  }
  .side-panel {
    position: absolute; left: 0; right: 0; top: 150px; height: 890px;
    background: var(--blue-deep);
    padding: 70px 14px 0;
    color: var(--white);
  }
  .side-stripe {
    position: absolute; left: 0; right: 0; height: 16px;
    background: var(--red);
  }
  .side-stripe--top { top: 36px; }
  .side-stripe--bottom { top: 850px; }
  .side-brand {
    color: var(--red); font-weight: 700; text-transform: uppercase;
    text-align: center; line-height: 1.05;
  }
  .side-brand__owner { font-size: 22px; }
  .side-brand__product { font-size: 32px; }
  .side-heading {
    margin-top: 90px;
    font-size: 34px; font-weight: 700; line-height: 1.1; text-align: center;
  }
  .side-directions-title {
    margin-top: 24px;
    font-size: 26px; font-weight: 700; text-align: center;
  }
  .side-directions {
    margin-top: 10px;
    font-size: 15px; line-height: 1.55;
  }
</style>
</head>
<body>
  <main class="bag-front" aria-label="Pellow's Golden Coat 10 lb bag, front panel">
    <section class="main-panel">
      <div class="brand-box">
        <p class="brand-name brand-name__owner">Pellow's</p>
        <p class="brand-name brand-name__product">Golden<br>Coat<span class="trademark">®</span></p>
      </div>
    </section>
    <div class="edge-strip"></div>
    <div class="edge-accent edge-accent--top"></div>
    <div class="edge-accent edge-accent--bottom"></div>

    <section class="maker">
      <p class="maker__name">by HALVERN FOOD PRODUCTS</p>
      <p class="maker__address">418 MARLOW AVENUE<br>CEDAR FALLS, IOWA 50613</p>
    </section>

    <section class="selling-copy">
      <h1 class="selling-copy__title">THE ALL PURPOSE BREADING</h1>
      <p class="selling-copy__tag">SEALS JUICE IN-GREASE OUT</p>
      <p class="selling-copy__detail">Cooks two-pound chicken well done in 10 minutes (deep fat).</p>
      <p class="selling-copy__slogan">Chicken fried the GOLDEN COAT way<br>is fried chicken the right way.</p>
    </section>

    <div class="right-accent"></div>

    <section class="ingredients">
      Ingredients: flour, salt, non-fat milk solids,
      egg yolk, baking powder, corn starch,
      sugar and pepper.
    </section>

    <div class="net-weight-bar"></div>
    <p class="net-weight">NET WT. 10LBS</p>
  </main>

  <aside class="bag-side" aria-label="Side panel with cooking directions">
    <section class="side-panel">
      <span class="side-stripe side-stripe--top"></span>
      <p class="side-brand side-brand__owner">Pellow's</p>
      <p class="side-brand side-brand__product">Golden<br>Coat<span class="trademark">®</span></p>
      <h2 class="side-heading">FRYING<br>GOOD<br>FOOD</h2>
      <h3 class="side-directions-title">DIRECTIONS</h3>
      <p class="side-directions">Dip chicken in water, roll in dry dip, coat thoroughly. Fry small chicken 1 1/2 to 2# 10 minutes, over 2# 12 minutes or longer. For best results double dip onion rings, shrimp and oysters.</p>
      <span class="side-stripe side-stripe--bottom"></span>
    </section>
  </aside>
</body>
</html>
```